Need a logo and business card design for my electrical company.
Company name is Kestrel Volt Electrical
In the bottow right hand corner i need
E.C. 708291 for the momument till i get my contractors license number sent to me.
Design i want black back ground with a picture of Thor's hammer and lighting hitting the top of it.

Industry/Entity Type

Electrical

Contact Information for Business Card

Owner Dermot Ashby Phone number 0412873590 email kestrelvoltelectrical@wirepostmail.com facebook page Kestrel Volt Electrical

```html
<!DOCTYPE html>
<html lang="en">
<head>
<meta charset="utf-8">
<title>Kestrel Volt Electrical – Business Card</title>
<link rel="stylesheet" href="https://fonts.googleapis.com/css2?family=Arimo:wght@400;700&display=swap">
<style>
  :root {
    --backdrop: #e6e2dc;
    --card-black: #000000;
    --stripe-blue: #1f3dff;
    --stripe-cyan: #12e6ff;
    --brand-cyan: #14c8ff;
    --text-white: #ffffff;
    --icon-ink: #16306e;
  }
  * { margin: 0; padding: 0; box-sizing: border-box; }
  html, body {
    width: 1200px;
    height: 851px;
    overflow: hidden;
    background: var(--backdrop);
  }
  .card {
    position: absolute;
    left: 38px;
    top: 79px;
    width: 1125px;
    height: 693px;
    background: var(--card-black);
    font-family: "Arimo", Arial, sans-serif;
    color: var(--text-white);
    overflow: hidden;
  }
  .accent-stripe {
    position: absolute;
    left: 128px;
    top: 0;
    width: 62px;
    height: 100%;
    background: linear-gradient(to bottom,
      var(--stripe-blue) 0%,
      var(--stripe-cyan) 45%,
      var(--stripe-blue) 100%);
  }
  .bolt-area {
    position: absolute;
    left: 115px;
    top: 68px;
    width: 96px;
    height: 192px;
    background: linear-gradient(to bottom, #1f3dff 0%, #12e6ff 55%, #1f6dff 100%);
  }
  .owner-name {
    position: absolute;
    left: 202px;
    top: 266px;
    font-size: 35px;
    font-weight: 700;
    letter-spacing: 0.2px;
  }
  .contact-list { list-style: none; }
  .contact-item {
    position: absolute;
    left: 142px;
    display: flex;
    align-items: center;
    height: 46px;
    margin-top: -23px;
  }
  .contact-icon {
    width: 46px;
    height: 46px;
    flex: none;
  }
  .contact-text {
    margin-left: 18px;
    font-size: 29px;
    font-weight: 400;
    white-space: nowrap;
  }
  .contact-item.phone { top: 362px; }
  .contact-item.email { top: 427px; }
  .contact-item.web { top: 492px; }
  .contact-item.address { top: 558px; }
  .brand-name {
    position: absolute;
    left: 600px;
    top: 120px;
    width: 460px;
    font-weight: 700;
    font-size: 62px;
    line-height: 1.1;
    color: var(--brand-cyan);
  }
  .licence-number {
    position: absolute;
    right: 98px;
    top: 578px;
    font-size: 33px;
    font-weight: 400;
  }
</style>
</head>
<body>
  <article class="card">
    <div class="accent-stripe"></div>

    <div class="bolt-area" role="img" aria-label="Blue lightning bolt decoration"></div>

    <h1 class="owner-name">Dermot Ashby</h1>

    <ul class="contact-list">
      <li class="contact-item phone">
        <svg class="contact-icon" viewBox="0 0 46 46" aria-hidden="true">
          <circle cx="23" cy="23" r="20" fill="none" stroke="var(--icon-ink)" stroke-width="2.5"/>
          <path d="M17 12 q-4 3 -1 11 q4 9 11 12 q4 0 5 -2 l-4 -5 q-2 1 -4 0 q-4 -3 -5 -8 q0 -2 2 -3 z"
                fill="var(--icon-ink)"/>
        </svg>
        <span class="contact-text">0412873590</span>
      </li>
      <li class="contact-item email">
        <svg class="contact-icon" viewBox="0 0 46 46" aria-hidden="true">
          <rect x="4" y="11" width="38" height="24" fill="var(--icon-ink)"/>
          <polyline points="4,11 23,26 42,11" fill="none" stroke="#6fd8ff" stroke-width="2"/>
        </svg>
        <span class="contact-text">kestrelvoltelectrical@wirepostmail.com</span>
      </li>
      <li class="contact-item web">
        <svg class="contact-icon" viewBox="0 0 46 46" aria-hidden="true">
          <g fill="none" stroke="var(--icon-ink)" stroke-width="2.5">
            <circle cx="23" cy="23" r="19"/>
            <ellipse cx="23" cy="23" rx="8" ry="19"/>
            <line x1="23" y1="4" x2="23" y2="42"/>
            <line x1="4" y1="23" x2="42" y2="23"/>
            <path d="M8 13 h30 M8 33 h30"/>
          </g>
        </svg>
        <span class="contact-text">www.company.com</span>
      </li>
      <li class="contact-item address">
        <svg class="contact-icon" viewBox="0 0 46 46" aria-hidden="true">
          <polygon points="23,5 43,19 3,19" fill="var(--icon-ink)"/>
          <rect x="6" y="21" width="34" height="19" fill="var(--icon-ink)"/>
          <rect x="11" y="26" width="10" height="10" fill="#2aa6ff"/>
          <rect x="25" y="26" width="10" height="10" fill="#2aa6ff"/>
        </svg>
        <span class="contact-text">Address</span>
      </li>
    </ul>

    <p class="brand-name">Kestrel Volt<br>Electrical</p>

    <p class="licence-number">E.C. 708291</p>
  </article>
</body>
</html>
```